RT Coinvault Corporate Letterhead

I have a corporate logo (uploaded). However, it may not be high enough quality for printing purposes, so the logo may need some work. I have a sample of letterhead (uploaded) that we currently use for electronic purposes only. The new design for letterhead does NOT need to look like the current electronic version -- in fact, I would prefer it doesn't. Additionally, I would like to be able to print this through pressly.example. If your design includes something on the reverse side of the paper, that's okay (even cool!) -- pressly.example can easily handle the printing of this. In summary I would like a letterhead design for print purposes, as well as an electronic version of the letterhead (to replace our current version) that can be used with Microsoft Word. Also, if you want to see how the logo on our website looks, go to www.rtcoinvault.example.

Colors
3277b5

Requirements
Must have
• At least the front side of a letterhead design using our current logo. A backside of the letterhead is optional. Must be able to print through pressly.example. Also must have an electronic version of the final design to use with Microsoft Word. Also, if the logo I uploaded isn't high enough quality, the logo will need to be enhanced for printing purposes. The color that I picked on Sketchora's color wheel may not be the correct blue, so feel free to change that if necessary. Also, the address and website address can be in a contrasting color chosen by the designer.
Nice to have
• I like original ideas/designs. So have fun with it!
Should not have
• Colors that are not in our current logo. If you would like to view it on our website, got to www.rtcoinvault.example

```html
<!DOCTYPE html>
<html lang="en">
<head>
<meta charset="utf-8">
<title>RT Coinvault Letterhead</title>
<link rel="stylesheet" href="https://fonts.googleapis.com/css2?family=Montserrat:wght@400;600&display=swap">
<style>
  :root {
    --brand-blue: #2f84f3;
    --paper: #ffffff;
    --trim: #111111;
  }
  html, body {
    margin: 0;
    padding: 0;
    overflow: hidden;
    background: var(--paper);
  }
  .letterhead {
    position: relative;
    width: 931px;
    height: 1200px;
    overflow: hidden;
    background: var(--paper);
    font-family: "Montserrat", sans-serif;
  }
  .letterhead__art {
    position: absolute;
    inset: 0;
  }
  .brand-name {
    position: absolute;
    left: 82px;
    width: 308px;
    top: 72px;
    text-align: center;
    font-weight: 600;
    font-size: 31px;
    letter-spacing: 0.5px;
    color: var(--brand-blue);
    line-height: 1;
    white-space: nowrap;
  }
  .contact {
    position: absolute;
    left: 429px;
    margin: 0;
    font-weight: 400;
    font-size: 12.6px;
    letter-spacing: 0.2px;
    line-height: 1;
    white-space: nowrap;
  }
  .contact--web {
    top: 84px;
    color: var(--paper);
  }
  .contact--address {
    top: 112px;
    color: var(--brand-blue);
  }
</style>
</head>
<body>
  <div class="letterhead">
    <svg class="letterhead__art" width="931" height="1200" viewBox="0 0 931 1200" aria-hidden="true">
      <rect class="header-band" x="0" y="0" width="931" height="101.6" fill="var(--brand-blue)"/>
      <path class="header-tab" d="M81.8,101.6 L86.8,81.6 Q91.6,64.3 109.6,64.3 L361.5,64.3 Q379.5,64.3 384.4,81.6 L389.5,101.6 Z" fill="var(--paper)"/>
      <rect class="footer-band" x="0" y="1170.5" width="931" height="29.5" fill="var(--brand-blue)"/>
      <g class="trim-marks" stroke="var(--trim)" stroke-width="0.6" fill="none">
        <line x1="0" y1="8.2" x2="931" y2="8.2"/>
        <line x1="0" y1="1191" x2="931" y2="1191"/>
        <line x1="8.2" y1="0" x2="8.2" y2="1200"/>
        <line x1="922.3" y1="0" x2="922.3" y2="1200"/>
      </g>
    </svg>

    <div class="brand-name">RT Coinvault</div>
    <p class="contact contact--web">www.rtcoinvault.example</p>
    <p class="contact contact--address">4120 Meridian Parkway, Suite 310, Fairview, Texas 75069</p>
  </div>
</body>
</html>
```